Museum quality exhibition portfolio

Create a museum-quality exhibition portfolio documenting the acquisition of several works by Danish artist Karen Vindahl.
This publication will be presented as an anniversary gift before the artwork arrives from Denmark.
The recipient should feel as though he has been invited into a private gallery to experience the collection before it enters his home.
This is not a coffee table book.
This is not a photo album.
This is not a scrapbook.
It should feel like a publication sold in the bookstore of a world-class Scandinavian museum. The copy is in the file COPY and CONTENT I will be printing only 5 copies of this and it's primarily for my Husband for our anniversary as I purchased these works of arts shown in the moon board attachments. I also need the final file that I can send to a printer who will print on high quality paper.

```html
<!DOCTYPE html>
<html lang="en">
<head>
<meta charset="utf-8">
<title>The Marlowe Ashford Collection — A Private Exhibition</title>
<link rel="stylesheet" href="https://fonts.googleapis.com/css2?family=Playfair+Display:wght@400;500;700&family=Libre+Baskerville:ital,wght@0,400;0,700;1,400&family=Jost:wght@400;500;600&display=swap">
<style>
:root{
  --backdrop:#9d9d9d;
  --paper:#eeebe2;
  --white:#ffffff;
  --gold:#b08a3f;
  --ink:#2f2d2a;
  --ink-soft:#55524c;
  --wood-dark:#4f3321;
  --wood-mid:#7b5637;
  --wood-light:#9a7550;
}
*{margin:0;padding:0;box-sizing:border-box}
html,body{width:1200px;height:4800px;overflow:hidden}
body{background:var(--backdrop);position:relative;color:var(--ink);font-family:"Libre Baskerville",Georgia,serif}
.spread{position:absolute;left:121px;width:958px;height:611px;display:flex;box-shadow:0 1px 3px rgba(0,0,0,.12)}
.page{position:relative;width:479px;height:611px;background:var(--paper);overflow:hidden}
.page--white{background:var(--white)}
.title{font-family:"Playfair Display",Georgia,serif;font-weight:400;color:var(--ink);letter-spacing:.02em}
.title__the{display:block;font-size:22px;line-height:26px}
.title__line{display:block;font-size:50px;line-height:60px}
.kicker{font-family:"Jost",Arial,sans-serif;color:var(--gold);font-weight:500}
.cover-title{position:absolute;left:74px;top:170px}
.cover-kicker{position:absolute;left:76px;top:408px;font-size:15px}
.frontis{position:absolute;left:0;width:479px;top:80px;text-align:center}
.frontis .title__the{font-size:20px;line-height:24px}
.frontis .title__line{font-size:44px;line-height:54px}
.frontis .kicker{display:block;font-size:14px;margin-top:22px}
.credits{margin-top:34px;font-family:"Playfair Display",Georgia,serif;font-weight:400;font-size:13px;line-height:21px;color:var(--ink)}
.credits b{font-weight:700}
.credits p{margin-bottom:16px}
.epigraph{position:absolute;left:0;width:479px;top:220px;text-align:center}
.epigraph__mark{display:block;width:14px;height:14px;border-radius:50%;background:var(--gold);margin:0 auto 22px}
.epigraph p{font-family:"Playfair Display",Georgia,serif;color:var(--gold);font-size:19px;line-height:31.5px}
.section-head{position:absolute;left:74px;font-family:"Jost",Arial,sans-serif;color:var(--gold);font-weight:500;font-size:14px;line-height:18px;letter-spacing:.01em;text-transform:uppercase}
.body-copy{position:absolute;font-size:6.6px;line-height:9.4px;color:var(--ink-soft)}
.body-copy p{margin-bottom:6px}
.rule{position:absolute;left:75px;width:41px;height:1.5px;background:var(--gold)}
.folio{position:absolute;bottom:20px;font-family:"Jost",Arial,sans-serif;font-size:5.5px;font-weight:600;letter-spacing:.08em;color:var(--ink);text-transform:uppercase}
.folio--left{left:20px}
.folio--right{right:20px}
.folio span{color:var(--gold);margin-right:6px}
.chapter{position:absolute;left:253px;top:266px;font-family:"Jost",Arial,sans-serif;font-weight:600;color:var(--gold);font-size:32px;line-height:38px}
.chapter__rule{position:absolute;left:254px;top:346px;width:67px;height:1.5px;background:var(--gold)}
.work-number{position:absolute;left:78px;top:258px;font-family:"Jost",Arial,sans-serif;font-weight:400;color:var(--gold);font-size:30px}
.work-title{position:absolute;left:78px;top:320px;font-family:"Jost",Arial,sans-serif;font-weight:600;color:var(--gold);font-size:10px;letter-spacing:.06em}
.work-notes{position:absolute;left:78px;top:346px;width:245px;font-family:"Jost",Arial,sans-serif;font-size:6.4px;line-height:8.4px;color:var(--ink)}
.work-notes b{font-weight:600;display:block}
.work-notes p{margin-bottom:6px}
.plate{position:absolute;background:linear-gradient(135deg,var(--wood-light) 0%,var(--wood-mid) 45%,var(--wood-dark) 100%)}
</style>
</head>
<body>

<section class="spread" style="top:140px">
  <div class="page page--white"></div>
  <div class="page">
    <h1 class="title cover-title">
      <span class="title__the">THE</span>
      <span class="title__line">MARLOWE</span>
      <span class="title__line">ASHFORD</span>
      <span class="title__line">COLLECTION</span>
    </h1>
    <p class="kicker cover-kicker">A Private Exhibition</p>
  </div>
</section>

<section class="spread" style="top:792px">
  <div class="page"></div>
  <div class="page">
    <div class="frontis">
      <h2 class="title">
        <span class="title__the">THE</span>
        <span class="title__line">MARLOWE</span>
        <span class="title__line">ASHFORD</span>
        <span class="title__line">COLLECTION</span>
      </h2>
      <span class="kicker">A Private Exhibition</span>
      <div class="credits">
        <p>Works by<br><b>Karen Vindahl</b></p>
        <p>Collected by<br>Theodore Ashford</p>
        <p>For</p>
        <p>Everett Marlowe<br>Anniversary Edition<br>July 2026</p>
      </div>
    </div>
  </div>
</section>

<section class="spread" style="top:1444px">
  <div class="page">
    <div class="epigraph">
      <span class="epigraph__mark"></span>
      <p>Some collections<br>begin with a purchase.<br>The best ones begin<br>with a story.</p>
    </div>
    <p class="folio folio--left"><span>2</span>The Marlowe Ashford Collection</p>
  </div>
  <div class="page">
    <h2 class="section-head" style="top:64px">Letter from Theo</h2>
    <div class="body-copy" style="left:74px;top:124px;width:380px">
      <p>Dear Everett,</p>
      <p>There are some things worth waiting for, and some things worth crossing an ocean for. These are both. This book is a small preview of a collection that is still on its way home.</p>
      <p>The works remain in Copenhagen until the exhibition closes in the autumn, and they will not arrive until the light has already turned. I did not want you to meet them for the first time through the side of a wooden crate.</p>
      <p>When we first stood in the studio you asked very little and looked for a long time. I watched you return to the same pieces again and again, as if they had already chosen you long before we chose them. That is when I knew.</p>
      <p>Karen works slowly. Each piece is shaped by hand, tested, set aside and returned to. Nothing is rushed and nothing is decoration for its own sake. I think that is why you trusted her work at once, and why I trust it now.</p>
      <p>Over the years we have collected moments more than things. A table built from an old barn floor. A print from a harbour town. A letter kept in a drawer for far too long. This collection belongs with those.</p>
      <p>The pages that follow are arranged the way a small gallery might present them: the artist first, then the works, one at a time, with room to pause between them.</p>
      <p>Read them slowly. Come back to them. By the time the first crate arrives, I hope each piece will already feel familiar, like a guest we have been expecting.</p>
      <p>Some works ask to be noticed. Others quietly ask to become part of your life. These are the second kind.</p>
      <p>Happy anniversary. Here is to the years behind us and all the rooms still waiting to be filled.</p>
      <p>With love,<br>Theo, always</p>
    </div>
    <p class="folio folio--right">3</p>
  </div>
</section>

<section class="spread" style="top:2094px">
  <div class="page">
    <span class="rule" style="top:88px"></span>
    <div class="body-copy" style="left:75px;top:124px;width:330px">
      <p>Why a private exhibition</p>
      <p>Every collection tells a story long before anything hangs on a wall. This one began with a single afternoon and a long conversation about what we wanted our home to feel like.</p>
      <p>This collection is not meaningful only because it was made by an accomplished artist whose work appears in respected rooms across Denmark. It matters because it was chosen together, for us, for the next chapter of our life.</p>
      <p>These works arrived in our story at exactly the right moment.</p>
      <p>In a quiet studio by the water, the artist talked about how every object she makes is meant to be held, lived with and returned to. Nothing here was made to sit behind glass.</p>
      <p>Perhaps that is why, while walking through her rooms, we kept stopping at the same shelf.</p>
      <p>Enjoy the journey.</p>
      <p>Beautiful tools, carefully made.<br>Quiet forms.<br>Honest materials.<br>Gentle light.</p>
      <p>Altogether they are the works we return to, and the ones we would keep if we could only keep a few. Without saying a word, they remind us of the places we have been and the things we still hope to do.</p>
      <p>This book is the first room of that exhibition. The rest will follow when the works come home.</p>
      <p>It is a gift that does not end with unwrapping. It continues every time we pass it in the hallway or take one of the pieces in hand.</p>
      <p>They begin as objects of craft.</p>
      <p>They become part of a home, and then, slowly, part of a marriage. Each carries a small memory of the day we found it, and the many days we will spend with it after.</p>
      <p>Enjoy the journey.</p>
      <p>All my love</p>
    </div>
    <p class="folio folio--left"><span>4</span>The Marlowe Ashford Collection</p>
  </div>
  <div class="page">
    <h2 class="section-head" style="top:56px">The artist behind<br>the collection</h2>
    <div class="body-copy" style="left:74px;top:91px;width:380px">
      <p>There are artists whose work you admire from a distance, and artists whose work you want to live beside every single day.</p>
      <p>Karen Vindahl belongs to the second kind.</p>
      <p>Working between Copenhagen and the islands south of the city, Karen creates sculptural objects, functional tools and small works that sit somewhere between art and craft. Using reclaimed metal, forged silver and salvaged wood, she gives new purpose to materials that might otherwise be lost, and finishes each piece by hand.</p>
      <p>Her practice has earned recognition across Scandinavia, with exhibitions in Copenhagen, Aarhus and Malmö, and her work is held in several private collections. She is known for an unhurried method: a form may be made and remade many times before it leaves her bench.</p>
      <p>What makes Karen's work remarkable is not only its technical mastery.</p>
      <p>It is her conviction.</p>
      <p>Every object begins with a question about how it will be used, held and remembered. Form follows the hand. Ornament is rare and always earned, and surfaces are left to wear gently over the years.</p>
      <p>Perhaps that is why her work feels so at home in the rooms where people actually live.</p>
      <p>Nothing is accidental.</p>
      <p>Everything has purpose.</p>
      <p>For us, her work became something we kept returning to long after we left the studio.</p>
      <p>Years before we met her, we had admired a small forged piece in a friend's kitchen in Copenhagen. We remembered it for a long time without knowing the name of the maker. Finding her studio felt less like a discovery and more like a reunion.</p>
      <p>The pieces in this collection were chosen with that feeling in mind.</p>
      <p>Karen describes her studio as a place of patience. Tools hang in the order they are used. Drawings are pinned beside half finished forms, and the light from the harbour changes the colour of the metal through the afternoon.</p>
      <p>When we visited in Copenhagen, she spoke about the people who will one day hold her work, and about the quiet, daily moments a well made object can make a little better. It is a hope we now share.</p>
    </div>
    <p class="folio folio--right">5</p>
  </div>
</section>

<section class="spread" style="top:2746px">
  <div class="page">
    <span class="rule" style="top:89px"></span>
    <div class="body-copy" style="left:75px;top:138px;width:330px">
      <p>These works are the first of the collection to enter our home.</p>
      <p>The works themselves remain on exhibition in Denmark as we read these pages. They are still being shown to visitors in a quiet gallery by the harbour, and they will travel to us once the season closes. Until then, this book stands in their place.</p>
      <p>Before the crates arrive, we have already started to imagine their places on our walls and shelves: one in the hall, one by the window, one near the table where we share our mornings. Each will find its own spot.</p>
      <p>Some of the pieces are small. Others ask for room.</p>
      <p>They were not bought as investments.</p>
      <p>They were chosen to remember the moments we have shared, the places we have travelled, and the ones we have yet to reach.</p>
      <p>Turn the page slowly. The exhibition begins here, one work at a time.</p>
    </div>
    <p class="folio folio--left"><span>6</span>The Marlowe Ashford Collection</p>
  </div>
  <div class="page">
    <h2 class="chapter">THE<br>COLLECTION</h2>
    <span class="chapter__rule"></span>
    <p class="folio folio--right">7</p>
  </div>
</section>

<section class="spread" style="top:3396px">
  <div class="page">
    <p class="work-number">01</p>
    <h3 class="work-title">HARBOUR LIGHT</h3>
    <div class="work-notes">
      <p><b>Karen Vindahl</b>Forged silver with turned oak collar, brushed finish<br>Marlowe Ashford Collection<br>Acquired July 2026</p>
      <p><b>Karen's Words</b>(Insert Karen's artist statement / original description for the work)</p>
      <p><b>Theo's Reflection</b>Some works ask to be noticed. Others quietly ask to become part of your life.</p>
      <p>A keepsake made for us to hold and to use. The first time we saw it, I was not thinking about where it would hang or what it would match. I thought of our mornings, the road ahead of us and the quiet routines that make a life. It was chosen for the next twenty years, not for a shelf, and it already feels like ours.</p>
    </div>
    <p class="folio folio--left"><span>8</span>The Marlowe Ashford Collection</p>
  </div>
  <div class="page">
    <div class="plate" style="left:0;top:0;width:479px;height:611px" role="img" aria-label="Photograph of a forged silver handle resting on a wooden board covered in handwritten notes"></div>
  </div>
</section>

<section class="spread" style="top:4047px">
  <div class="page">
    <p class="work-number">02</p>
    <h3 class="work-title">GRAIN STUDY</h3>
    <div class="work-notes">
      <p><b>Karen Vindahl</b>Engraved silver with blackened steel rings, hand polished<br>Marlowe Ashford Collection<br>Acquired July 2026</p>
      <p><b>Karen's Words</b>(Insert Karen's artist statement / original description for the work)</p>
      <p><b>Theo's Reflection</b>Some works ask to be noticed. Others quietly ask to become part of your life.</p>
      <p>A keepsake made for us to hold and to use. The first time we saw it, I was not thinking about where it would hang or what it would match. I thought of our mornings, the road ahead of us and the quiet routines that make a life. It was chosen for the next twenty years, not for a shelf, and it already feels like ours.</p>
    </div>
    <p class="folio folio--left"><span>10</span>The Marlowe Ashford Collection</p>
  </div>
  <div class="page">
    <div class="plate" style="left:0;top:61px;width:479px;height:460px" role="img" aria-label="Close photograph of an engraved silver tool lying on a dark wooden board with handwritten lettering"></div>
    <p class="folio folio--right">11</p>
  </div>
</section>

</body>
</html>
```